Podcast cover art (not a logo)

I’m launching an audio-only podcast for parents of neurodivergent children. The podcast is meant to feel like a calm, trusted professional voice — not a brand or a performance.

Style direction:
--Clean and minimal
--Calm and grounded
--Professional, not playful
--Nothing flashy, loud, or busy
--No cartoon imagery

Content on the cover:
--Podcast title: Under the Quiet Surface
--Subtitle or tagline: Supporting Neurodivergent Kids with Science, Not Shame (or Understanding Neurodivergent Kids)
--No episode numbers, no dates

Design preferences:
--Text-forward design
--Neutral or soft colors (muted blues, grays, off-whites)
--High contrast for readability at small sizes
--Simple, timeless font

What I do NOT want:
--A logo or branding system
--Illustrations of children or families
--Bright colors or playful graphics
--Trendy fonts or visual effects

Technical requirements:
--Square image
--3000 × 3000 pixels
--RGB color mode
--JPEG or PNG
--File size under 500 KB

Deliverables:
--Final cover art file
--Optional: one or two alternate background color versions

```html
<!DOCTYPE html>
<html lang="en">
<head>
<meta charset="utf-8">
<title>Under the Quiet Surface — Podcast Cover</title>
<link href="https://fonts.googleapis.com/css2?family=Gelasio:wght@600&family=Figtree:wght@300&display=swap" rel="stylesheet">
<style>
  :root {
    --bg: #818f95;
    --ink: #2f3538;
    --cream: #e2d8c6;
  }
  html, body {
    margin: 0;
    padding: 0;
    width: 1200px;
    height: 1200px;
    overflow: hidden;
    background: var(--bg);
  }
  .cover {
    width: 1200px;
    height: 1200px;
    box-sizing: border-box;
    display: flex;
    flex-direction: column;
    align-items: center;
    justify-content: center;
    text-align: center;
    padding-bottom: 20px;
  }
  .cover__title {
    margin: 0;
    font-family: "Gelasio", Georgia, serif;
    font-weight: 600;
    font-size: 104px;
    line-height: 138px;
    letter-spacing: -1px;
    color: var(--ink);
  }
  .cover__tagline {
    margin: 50px 0 0;
    font-family: "Figtree", Helvetica, Arial, sans-serif;
    font-weight: 300;
    font-size: 38px;
    line-height: 64px;
    letter-spacing: 0.5px;
    color: var(--cream);
  }
</style>
</head>
<body>
  <main class="cover">
    <h1 class="cover__title">Under the Quiet<br>Surface</h1>
    <p class="cover__tagline">Supporting Neurodivergent Kids<br>with Science, Not Shame</p>
  </main>
</body>
</html>
```